Flyer/Poster design required for volunteer activities

We need a STRIKING A4 Poster/Flyer advertising our conservation volunteer program activities which are currently happening in the area. This poster is to advertise the program once people have arrived on the island or to locals. The program covers 5 months, May-September 2019 and is focused on conservation. I have attached the following:
- a flyer which was previously created (Tidewatch Habitat Helpers 2019 sm)to advertise the program - would prefer it has a similar striking resemblance, but not essential
- A mock up document 'TWHH On Island Poster_2019_v2' with text -Logos-Images

Target Market(s)

Everyone interested in Environmental Adventure/Hiking/Citizen Science

Industry/Entity Type

Tourism

Font styles to use
Sans Serif

Requirements
Must have
• -A travel conservation focus
• -Must use 'Tidewatch-Background Image' as the background to the design
• -The info of where to get more information and the social media details must be prominent

```html
<!DOCTYPE html>
<html lang="en">
<head>
<meta charset="utf-8">
<title>Tidewatch Habitat Helpers – Volunteer Program 2019</title>
<link href="https://fonts.googleapis.com/css2?family=Bebas+Neue&family=Arimo:wght@400;700&display=swap" rel="stylesheet">
<style>
:root{
  --page:#f1f1ef;
  --yellow:#fde13a;
  --navy:#1f3f8f;
  --ink:#1c1c1c;
  --white:#ffffff;
  --sea-deep:#0f3f78;
  --sea:#2a7fb8;
  --sea-light:#5fb4d6;
  --land:#4d6a2c;
  --land-light:#8da05a;
}
*{margin:0;padding:0;box-sizing:border-box}
html,body{width:1200px;height:792px;overflow:hidden;background:var(--page)}
body{position:relative;font-family:"Arimo",Arial,sans-serif}
.poster{position:absolute;left:317px;top:0;width:566px;height:792px;background:var(--yellow)}
.backdrop{position:absolute;left:35px;top:29px;width:497px;height:741px;
  background:
    radial-gradient(ellipse 60% 45% at 12% 88%,var(--land-light),transparent 70%),
    radial-gradient(ellipse 45% 70% at 8% 70%,var(--land),transparent 70%),
    radial-gradient(ellipse 50% 20% at 80% 8%,#6b7d6a,transparent 70%),
    linear-gradient(180deg,#8fb2c9 0%,var(--sea-light) 10%,var(--sea) 35%,var(--sea-deep) 75%,#1c3a4e 100%)}
.display{font-family:"Bebas Neue",Impact,sans-serif;letter-spacing:.3px}
.title-line{position:absolute;left:86px;background:var(--ink);color:var(--yellow);font-size:43px;line-height:44px;padding:2px 12px 0;white-space:nowrap}
.title-1{top:72px}
.title-2{top:116px}
.tagline{position:absolute;left:86px;top:168px;width:306px;height:30px;background:var(--white);color:var(--navy);font-size:22px;line-height:31px;text-align:center;white-space:nowrap}
.intro{position:absolute;left:86px;top:203px;color:var(--white);font-size:14px;white-space:nowrap}
.badge{position:absolute;left:415px;top:168px;width:72px;height:72px;border-radius:50%;background:var(--white);border:3px solid var(--navy);color:var(--navy);font-size:22px;display:flex;align-items:center;justify-content:center}
.event{position:absolute}
.event .photo{position:absolute;left:0;top:0;width:96px;height:96px;border-radius:50%;border:3px solid var(--yellow)}
.event .month{position:absolute;left:100px;top:24px;background:var(--navy);color:var(--white);font-size:17px;line-height:19px;padding:0 5px;white-space:nowrap}
.event .theme{position:absolute;left:100px;top:44px;font-size:12px;line-height:15.5px;color:var(--ink);white-space:nowrap}
.event .theme span{display:inline-block;background:var(--yellow);padding:0 4px;margin-bottom:1px;white-space:nowrap}
.event .dates{position:absolute;left:100px;height:13px;background:var(--ink);color:var(--white);font-size:8px;line-height:13px;padding:0 6px 0 3px;display:flex;align-items:center;gap:4px;white-space:nowrap}
.dates svg{width:9px;height:9px}
.details{position:absolute;list-style:none;color:var(--white);font-size:7.4px;line-height:9.6px;text-shadow:0 0 2px rgba(0,0,0,.6)}
.divider{position:absolute;left:286px;top:432px;width:1px;height:82px;background:var(--white)}
.connector{position:absolute;left:268px;top:473px;width:18px;height:1px;background:var(--white)}
.footer{position:absolute;left:35px;top:728px;width:497px;height:42px;background:var(--navy);color:var(--white);text-align:center}
.footer .more{font-size:8.3px;font-weight:700;margin-top:6px;white-space:nowrap}
.footer .follow{display:flex;justify-content:center;align-items:center;gap:8px;margin-top:6px;font-size:8.3px;font-weight:700}
.follow .label{font-family:"Bebas Neue",Impact,sans-serif;font-size:13px;font-weight:400}
.follow .dot{width:8px;height:8px;background:var(--yellow);display:inline-block}
.follow .gap{width:14px}
</style>
</head>
<body>
<main class="poster">
  <div class="backdrop" role="img" aria-label="Aerial photograph of the island coastline, lagoon and mountains"></div>

  <h1 class="display">
    <span class="title-line title-1">Tidewatch Habitat</span>
    <span class="title-line title-2">Helpers Volunteers</span>
  </h1>
  <p class="tagline display">Be involved in protecting paradise</p>
  <p class="intro display">Join the Tidewatch Habitat Helpers program 2019</p>
  <div class="badge display">TWHH</div>

  <section class="event" style="left:77px;top:241px">
    <div class="photo" role="img" aria-label="Photo of a seabird chick" style="background:radial-gradient(circle at 45% 50%,#a9a49a,#5d6b3d 75%)"></div>
    <div class="month display">May 2019</div>
    <div class="theme display"><span>Birds of</span><br><span>Tidewatch Island</span></div>
    <div class="dates display" style="top:77px"><svg viewBox="0 0 10 10"><circle cx="5" cy="5" r="5" fill="#fde13a"/><path d="M3 5h4M5 3l2 2-2 2" stroke="#1c1c1c" stroke-width="1.3" fill="none"/></svg>16th – 28th May</div>
  </section>
  <ul class="details" style="left:81px;top:345px;width:200px">
    <li>-Ocean bird watching boat trips</li>
    <li>-Guided tours of Woodhen and Currawong quarters</li>
    <li>-Weekly lectures at the Tidewatch Island Museum</li>
    <li>-Weekly screenings of documentaries on Bird and Island Conservation projects</li>
    <li>-Self guided land bird survey tours</li>
  </ul>

  <section class="event" style="left:295px;top:241px">
    <div class="photo" role="img" aria-label="Photo of a snorkeller recording marine data underwater" style="background:radial-gradient(circle at 50% 55%,#6fa4c4,#1e4d78 75%)"></div>
    <div class="month display">June 2019</div>
    <div class="theme display"><span>Tidewatch Island</span><br><span>Marine Park</span></div>
    <div class="dates display" style="top:77px"><svg viewBox="0 0 10 10"><circle cx="5" cy="5" r="5" fill="#fde13a"/><path d="M3 5h4M5 3l2 2-2 2" stroke="#1c1c1c" stroke-width="1.3" fill="none"/></svg>3rd – 6th June</div>
  </section>
  <ul class="details" style="left:299px;top:345px;width:210px">
    <li>-Marine pest monitoring with marine park staff</li>
    <li>-Marine plastic &amp; debris clean up activities</li>
    <li>-Screenings of marine conservation documentaries at the museum</li>
    <li>-Weekly lectures on Marine Life at the Tidewatch Island Museum</li>
    <li>-Marine Activities with local operators</li>
  </ul>

  <section class="event" style="left:77px;top:421px">
    <div class="photo" role="img" aria-label="Photo of a hiker on a green mountain cliff path" style="background:radial-gradient(circle at 40% 45%,#9aa08a,#3d5a2a 75%)"></div>
    <div class="month display">July 2019</div>
    <div class="theme display"><span>Invasive</span><br><span>Species</span></div>
    <div class="dates display" style="top:77px"><svg viewBox="0 0 10 10"><circle cx="5" cy="5" r="5" fill="#fde13a"/><path d="M3 5h4M5 3l2 2-2 2" stroke="#1c1c1c" stroke-width="1.3" fill="none"/></svg>21st – 28th July</div>
  </section>
  <div class="connector"></div>
  <div class="divider"></div>
  <ul class="details" style="left:299px;top:432px;width:160px">
    <li>-Guided walks to learn about the weed eradication program</li>
    <li>-Weekly lectures on plants of Tidewatch Island</li>
    <li>-Weekly screenings of documentaries on plant and island conservation projects</li>
    <li>-Guided walks to Mount Corran</li>
    <li>-Local tour guides include commentaries on island plants</li>
  </ul>

  <section class="event" style="left:77px;top:539px">
    <div class="photo" role="img" aria-label="Photo of volunteers gathered around a field specimen tray" style="background:radial-gradient(circle at 50% 55%,#b7b3a3,#4f5e3b 75%)"></div>
    <div class="month display">August 2019</div>
    <div class="theme display"><span>Amazing</span><br><span>Invertebrates</span></div>
    <div class="dates display" style="top:77px"><svg viewBox="0 0 10 10"><circle cx="5" cy="5" r="5" fill="#fde13a"/><path d="M3 5h4M5 3l2 2-2 2" stroke="#1c1c1c" stroke-width="1.3" fill="none"/></svg>11th – 16th August</div>
  </section>
  <ul class="details" style="left:81px;top:644px;width:200px">
    <li>-Guided night walks to learn about the island's invertebrates</li>
    <li>-Weekly viewing and presentation of the Tidewatch Island Phasmid</li>
    <li>-Weekly lectures on invertebrates of Tidewatch Island at the museum</li>
    <li>-Weekly screenings of documentaries on island conservation projects</li>
  </ul>

  <section class="event" style="left:295px;top:539px">
    <div class="photo" role="img" aria-label="Photo of a large stick insect resting on an open hand" style="background:radial-gradient(circle at 50% 50%,#e0b9a6,#9a7466 75%)"></div>
    <div class="month display">September 2019</div>
    <div class="theme display"><span>Protecting</span><br><span>Paradise</span></div>
    <div class="dates display" style="top:77px"><svg viewBox="0 0 10 10"><circle cx="5" cy="5" r="5" fill="#fde13a"/><path d="M3 5h4M5 3l2 2-2 2" stroke="#1c1c1c" stroke-width="1.3" fill="none"/></svg>1st – 6th September</div>
  </section>
  <ul class="details" style="left:299px;top:644px;width:222px">
    <li>-Observational snorkel surveys with Marine Ecologists, to assess populations of Banded Anemonefish and other unique fish species</li>
    <li>-Guided snorkel and glass bottom boat tour to assess coral health within the Tidewatch Island Marine Park</li>
    <li>-Guided walks to learn about the island's conservation history</li>
  </ul>

  <footer class="footer">
    <p class="more">See the Tidewatch visitor centre for more information about the Tidewatch Habitat Helpers program for 2019</p>
    <p class="follow">
      <span class="label">Follow us!</span>
      <span class="dot"></span><span>www.friendsnet.com/twhh</span>
      <span class="gap"></span>
      <span class="dot"></span><span>snapgrid@twhh</span>
    </p>
  </footer>
</main>
</body>
</html>
```